Top Producing Realtor Business Card Design

Looking for branding with my logo on all of my materials. I am a top producing real estate agent, selling expensive homes in California. I'm looking for a classy design that includes my existing logo, the company corporate logo and my photo.

Looking forward to your submissions! Thank you so much! :)

I appreciate your submissions very much!  Excellent work!  I have revised the brief to be more clear about what I think I'm looking for.  Keep the submissions coming in!!  Thank you so much :)

Target Market(s)

Wealthy home buyers and sellers in California.

Industry/Entity Type

Real Estate

Requirements
Must have
• Must include:

Homestead Partners Logo

Below Homestead Partners Logo it must say: Santa Clarita (Helvetica font)

Complete address: 58317 Marlow Street
Santa Clarita, CA 91321

Phone number: 805.492.1157 cell
805.374.2291 VM 5814 office

My photo

My name: Meg Horvath (please make sure it's correct before you submit) :)

My MH Logo (if possible please keep logo colors the same)

"Realtor" with a reserved symbol after or below my name

My license number: CalBRE #04827715

My website: www.MegHorvathHomes.example

My email: Meg@MegHorvathHomes.example

Nice to have
• I'm open minded :) The main goal is to have the MH logo is on all of my material. For the business cards I sort of imagine my MH logo in the background, and I like a fade. I prefer the logo to be on the front of the card, and I like it on the back of the card too, So a two sided business card is ok.

I prefer the light blue Homestead Partners Logo submitted. Please note the light blue color must closely match :)

Another idea is the business card can be in the format of the yard sign photo submitted (maybe changed into the light blue color), to possibly be a business card that looks like the yard sign. The yard sign layout must closely match the example submitted due to corporate guidelines.

Basically I'm looking for something that will tie everything together with my photo and logo so it's well branded in the clients mind. :)

Should not have
• Please keep the logo's exactly as they are, including color...no need to change.

If you choose to use the yard sign example provided for the business card, Please do not change the basic layout of the yard sign submitted, I have to follow the corporate standards.

```html
<!DOCTYPE html>
<html lang="en">
<head>
<meta charset="utf-8">
<title>Meg Horvath – Business Card</title>
<link href="https://fonts.googleapis.com/css2?family=Montserrat:wght@400;600;700&family=Arimo:wght@400;700&display=swap" rel="stylesheet">
<style>
  :root {
    --page: #ffffff;
    --front-deep: #0654a4;
    --front-glow: #5f95d0;
    --back-blue: #5685c4;
    --back-glow: #6f9bd3;
    --white: #ffffff;
    --photo-light: #b9b9b9;
    --photo-dark: #2a2a2a;
  }
  * { margin: 0; padding: 0; box-sizing: border-box; }
  html, body { width: 1200px; height: 1000px; overflow: hidden; background: var(--page); }
  .canvas { position: relative; width: 1200px; height: 1000px; }

  .card { position: absolute; left: 271px; width: 659px; height: 399px; overflow: hidden; }
  .card-front {
    top: 87px;
    background: radial-gradient(ellipse 55% 70% at 50% 45%, var(--front-glow) 0%, var(--front-deep) 100%);
  }
  .watermark {
    position: absolute; left: 0; right: 0; top: 40px; text-align: center;
    font-family: "Montserrat", sans-serif; font-weight: 700; font-size: 380px; line-height: 1;
    color: var(--white); opacity: 0.12; letter-spacing: -10px;
  }
  .front-mark {
    position: absolute; left: 0; right: 0; top: 95px; text-align: center;
    font-family: "Montserrat", sans-serif; font-weight: 700; font-size: 120px; line-height: 1;
    color: var(--white);
  }
  .front-name {
    position: absolute; left: 0; right: 0; top: 265px; text-align: center;
    font-family: "Montserrat", sans-serif; font-weight: 700; font-size: 38px; color: var(--white);
  }
  .front-title {
    position: absolute; left: 0; right: 0; top: 310px; text-align: center;
    font-family: "Montserrat", sans-serif; font-weight: 400; font-size: 23px; letter-spacing: 1px; color: var(--white);
  }
  sup { font-size: 0.4em; vertical-align: super; }

  .card-back { top: 527px; background: var(--back-blue); }
  .portrait {
    position: absolute; left: 0; top: 0; width: 270px; height: 399px;
    background: radial-gradient(ellipse 70% 60% at 50% 35%, var(--photo-light) 0%, #8a8a8a 55%, var(--photo-dark) 100%);
  }
  .info-panel {
    position: absolute; left: 270px; top: 0; width: 389px; height: 399px;
    background: radial-gradient(ellipse 80% 70% at 60% 50%, var(--back-glow) 0%, var(--back-blue) 100%);
    color: var(--white);
  }
  .brokerage {
    position: absolute; left: 290px; top: 58px; width: 160px; text-align: center;
    font-family: "Arimo", sans-serif; font-weight: 700; font-size: 16px; line-height: 1.2;
  }
  .brokerage-city {
    position: absolute; left: 290px; top: 116px; width: 160px; text-align: center;
    font-family: "Arimo", sans-serif; font-size: 13px; letter-spacing: 0.3px;
  }
  .agent-mark {
    position: absolute; left: 490px; top: 30px; width: 120px; text-align: center;
    font-family: "Montserrat", sans-serif; font-weight: 700; font-size: 56px; line-height: 1;
  }
  .agent-name {
    position: absolute; left: 460px; top: 118px; width: 180px; text-align: center;
    font-family: "Montserrat", sans-serif; font-weight: 700; font-size: 19px;
  }
  .agent-title {
    position: absolute; left: 460px; top: 140px; width: 180px; text-align: center;
    font-family: "Montserrat", sans-serif; font-size: 12px; letter-spacing: 0.5px;
  }
  .contact {
    position: absolute; right: 54px; text-align: right;
    font-family: "Arimo", sans-serif; white-space: nowrap;
  }
  .license { top: 167px; font-size: 12px; }
  .address { top: 203px; font-size: 17px; line-height: 22px; }
  .phones { top: 250px; font-size: 18px; line-height: 25px; }
  .phones b { font-weight: 700; }
  .online { top: 316px; right: 58px; font-size: 18px; font-weight: 700; line-height: 24px; }
</style>
</head>
<body>
<div class="canvas">
  <section class="card card-front">
    <div class="watermark" aria-hidden="true">MH</div>
    <div class="front-mark">MH</div>
    <div class="front-name">Meg Horvath</div>
    <div class="front-title">REALTOR<sup>®</sup></div>
  </section>

  <section class="card card-back">
    <div class="portrait" role="img" aria-label="Black and white portrait photo of the agent"></div>
    <div class="info-panel"></div>
    <div class="brokerage" style="color:var(--white)">Homestead<br>Partners</div>
    <div class="brokerage-city" style="color:var(--white)">SANTA CLARITA</div>
    <div class="agent-mark" style="color:var(--white)">MH</div>
    <div class="agent-name" style="color:var(--white)">Meg Horvath</div>
    <div class="agent-title" style="color:var(--white)">REALTOR<sup>®</sup></div>
    <div class="contact license" style="color:var(--white)">CalBRE #04827715</div>
    <div class="contact address" style="color:var(--white)">58317 Marlow Street<br>Santa Clarita, CA 91321</div>
    <div class="contact phones" style="color:var(--white)"><b>805.492.1157</b> (Cell)<br><b>805.374.2291 VM 5814</b> (Office)</div>
    <div class="contact online" style="color:var(--white)">www.MegHorvathHomes.example<br>Meg@MegHorvathHomes.example</div>
  </section>
</div>
</body>
</html>
```